High End International Drug and Alcohol Recovery Service Needs a Brochure Design

We need a flyer design for a high end, private, drug, alcohol and addiction recovery firm. We are based in Los Angeles. We want the flyer to be a bi-fold or trifold. We want it to have a sleek, modern look but conveys the message that we are here to support our clients and help them through difficult times. We want to be approachable.
I am attaching picstures for you all to use.

Target Market(s)

High end clients, affluent clientele.

Industry/Entity Type

Life Coaching

Requirements
Must have
• Must have our logo on the back.
Nice to have
• Our slogans somewhere in there, "find your path" and "build your future."

```html
<!DOCTYPE html>
<html lang="en">
<head>
<meta charset="utf-8">
<title>Clearway Life Partners — Brochure</title>
<link rel="stylesheet" href="https://fonts.googleapis.com/css2?family=Montserrat:wght@400;600;800;900&family=Raleway:wght@300;400&family=Great+Vibes&family=Open+Sans:wght@400;600&display=swap">
<style>
  :root{
    --gold:#f2b71f;
    --gold-deep:#e0a30c;
    --ink:#1e1e1e;
    --charcoal:#2c2c2c;
    --grey:#7a7a7a;
    --grey-light:#a9a9a9;
    --paper:#ffffff;
    --backdrop:#ece8e2;
  }
  *{box-sizing:border-box;margin:0;padding:0}
  html,body{width:900px;height:1200px;overflow:hidden;background:var(--backdrop)}
  body{font-family:"Open Sans",Arial,sans-serif;color:var(--ink)}
  .canvas{position:relative;width:900px;height:1200px;display:flex;gap:20px;justify-content:center;align-items:center}
  .panel{position:relative;width:420px;height:594px;background:var(--paper);overflow:hidden;box-shadow:0 6px 18px rgba(0,0,0,.18)}

  /* ---------- Cover panel ---------- */
  .cover-header{position:absolute;left:0;top:0;width:420px;height:150px;background:var(--gold)}
  .cover-illustration{position:absolute;left:0;top:0;width:150px;height:150px;background:linear-gradient(135deg,#f6c94a 0%,#e9a80e 100%)}
  .cover-title{position:absolute;left:170px;top:30px;font-family:"Montserrat",sans-serif;color:var(--paper);line-height:1}
  .cover-title .lead{font-size:26px;font-weight:800;letter-spacing:.5px}
  .cover-title .main{font-size:44px;font-weight:900;letter-spacing:1px;margin-top:2px}
  .cover-title .slogan{font-size:17px;font-weight:800;color:var(--ink);margin-top:8px;letter-spacing:.5px}
  .cover-aside{position:absolute;left:14px;top:168px;width:126px;font-size:7.5px;line-height:1.55;color:var(--grey)}
  .cover-aside h3{font-family:"Montserrat",sans-serif;font-size:9px;font-weight:700;color:var(--gold-deep);margin-bottom:5px;text-transform:uppercase}
  .cover-aside p+p{margin-top:8px}
  .cover-photo{position:absolute;left:150px;top:150px;width:270px;height:300px;background:linear-gradient(180deg,#c9d8e6 0%,#9fb1c2 45%,#6e675d 75%,#4a433b 100%)}
  .brand-tile{position:absolute;left:290px;top:410px;width:112px;height:112px;background:var(--charcoal);display:flex;flex-direction:column;align-items:center;justify-content:center;gap:8px}
  .brand-mark{width:20px;height:20px;border:2px solid var(--gold)}
  .brand-tile .brand-name{font-family:"Raleway",sans-serif;font-weight:300;font-size:11px;color:var(--paper);text-align:center;line-height:1.3}
  .contact-list{position:absolute;left:18px;top:480px;list-style:none;font-size:8.5px;color:var(--grey)}
  .contact-list li{display:flex;align-items:center;gap:8px;margin-bottom:7px}
  .contact-list svg{width:13px;height:13px;flex:none}
  .call-bar{position:absolute;left:290px;top:534px;width:112px;height:26px;background:var(--gold);display:flex;align-items:center;justify-content:center;gap:6px;font-family:"Montserrat",sans-serif;font-size:9px;font-weight:700;color:var(--ink)}
  .call-bar svg{width:10px;height:10px}

  /* ---------- Inside panel ---------- */
  .inside-brand{position:absolute;left:18px;top:16px;font-family:"Raleway",sans-serif;font-weight:300;font-size:23px;line-height:1.1;color:var(--grey)}
  .inside-intro{position:absolute;left:228px;top:18px;width:176px;font-style:italic;font-size:8.5px;line-height:1.5;color:var(--charcoal)}
  .photo-couple{position:absolute;left:0;top:78px;width:200px;height:130px;background:linear-gradient(135deg,#d9c3a6 0%,#b0896a 50%,#6f5a4b 100%)}
  .services{position:absolute;left:222px;top:84px;width:180px}
  .services h4,.programs h4{font-family:"Montserrat",sans-serif;font-size:8px;font-weight:700;letter-spacing:1px;margin-bottom:5px}
  .services ul,.programs ul{list-style:none;font-size:7.5px;line-height:1.75;color:var(--grey)}
  .services li::before{content:"";display:inline-block;width:5px;height:5px;background:var(--gold);margin-right:6px;vertical-align:middle}
  .tagline-band{position:absolute;left:0;top:218px;width:420px;height:42px;background:var(--charcoal);display:flex;align-items:center;padding-left:24px;font-family:"Great Vibes",cursive;font-size:25px;color:var(--gold)}
  .headline{position:absolute;left:20px;top:278px;font-family:"Montserrat",sans-serif;font-weight:900;line-height:.95;color:var(--ink)}
  .headline .line{display:block;font-size:52px;letter-spacing:1px}
  .headline .accent{color:var(--gold)}
  .headline-script{position:absolute;left:20px;top:400px;font-family:"Great Vibes",cursive;font-size:24px;color:var(--grey)}
  .photo-calm{position:absolute;left:232px;top:272px;width:188px;height:120px;background:linear-gradient(135deg,#d8d2ca 0%,#a89c8e 55%,#6a6157 100%)}
  .photo-session{position:absolute;left:0;top:440px;width:210px;height:154px;background:linear-gradient(160deg,#5a5a5a 0%,#2f2f2f 100%)}
  .programs{position:absolute;left:210px;top:430px;width:210px;height:164px;background:var(--gold);padding:18px 22px}
  .programs h4{color:var(--ink)}
  .programs ul{color:var(--charcoal)}
  .programs li::before{content:"›";margin-right:6px;font-weight:700}
</style>
</head>
<body>
<main class="canvas">

  <section class="panel cover">
    <header class="cover-header">
      <div class="cover-illustration" role="img" aria-label="Illustration of a climber reaching a hand to help another up a slope"></div>
      <h1 class="cover-title">
        <span class="lead">BUILD YOUR</span>
        <span class="main" style="display:block">FUTURE</span>
        <span class="slogan" style="display:block">FIND YOUR PATH</span>
      </h1>
    </header>

    <div class="cover-aside">
      <h3>About Our Approach</h3>
      <p>Private, discreet recovery care shaped around each client, with calm support at every step.</p>
      <p>Our team walks beside you through difficult days toward lasting change.</p>
    </div>

    <div class="cover-photo" role="img" aria-label="Photo of one climber pulling another up a rock face against a pale sky"></div>

    <div class="brand-tile">
      <span class="brand-mark"></span>
      <span class="brand-name">Clearway<br>Life Partners</span>
    </div>

    <ul class="contact-list">
      <li>
        <svg viewBox="0 0 16 16"><circle cx="8" cy="8" r="8" fill="#f2b71f"/><path d="M5.2 4.5l1.4-.3.8 1.8-.9.7a5 5 0 0 0 2.8 2.8l.7-.9 1.8.8-.3 1.4c-3.4.2-6.5-2.9-6.3-6.3z" fill="#fff"/></svg>
        (555) 014-2280
      </li>
      <li>
        <svg viewBox="0 0 16 16"><circle cx="8" cy="8" r="8" fill="#f2b71f"/><circle cx="8" cy="8" r="4" fill="none" stroke="#fff" stroke-width="1"/><path d="M4 8h8M8 4c-1.6 2.2-1.6 5.8 0 8M8 4c1.6 2.2 1.6 5.8 0 8" fill="none" stroke="#fff" stroke-width="1"/></svg>
        www.clearwaylife.com
      </li>
      <li>
        <svg viewBox="0 0 16 16"><circle cx="8" cy="8" r="8" fill="#f2b71f"/><rect x="4" y="5.2" width="8" height="5.6" fill="none" stroke="#fff" stroke-width="1"/><path d="M4 5.4l4 3 4-3" fill="none" stroke="#fff" stroke-width="1"/></svg>
        info@clearwaylife.com
      </li>
    </ul>

    <div class="call-bar">
      <svg viewBox="0 0 16 16"><path d="M3 2l3-.5 1.5 3.5-1.8 1.3a9 9 0 0 0 4 4l1.3-1.8L14.5 10 14 13C8 13.5 2.5 8 3 2z" fill="#1e1e1e"/></svg>
      (555) 014-2280
    </div>
  </section>

  <section class="panel inside">
    <div class="inside-brand">Clearway<br>Life Partners</div>
    <p class="inside-intro">We believe in a diverse range of approaches to guide you toward the best possible experience.</p>

    <div class="photo-couple" role="img" aria-label="Photo of two people sitting together outdoors at sunset"></div>

    <div class="services">
      <h4>SERVICES</h4>
      <ul>
        <li>Sober companionship</li>
        <li>Life coaching</li>
        <li>Family mentoring</li>
        <li>Intervention support</li>
        <li>Aftercare planning</li>
        <li>Relapse prevention</li>
      </ul>
    </div>

    <div class="tagline-band">Mentoring · Companionship · Coaching</div>

    <h2 class="headline">
      <span class="line">FIND</span>
      <span class="line">YOUR</span>
      <span class="line accent">PATH</span>
    </h2>
    <div class="photo-calm" role="img" aria-label="Photo of hands resting in a meditation pose"></div>
    <p class="headline-script">Build Your Future</p>

    <div class="photo-session" role="img" aria-label="Photo of a quiet one-to-one coaching session"></div>
    <div class="programs">
      <h4>PROGRAMS</h4>
      <ul>
        <li>Recovery</li>
        <li>Wellness</li>
        <li>Mindfulness</li>
        <li>Life Skills</li>
        <li>Dual Diagnosis</li>
        <li>Executive Programs</li>
        <li>Family Healing</li>
      </ul>
    </div>
  </section>

</main>
</body>
</html>
```